Business Card Design Project

I would like to have a project of business card with incorporated attachted logo elements in warm colors like: gold, yellow, brown.
We would like incorporate below information into the design
Name of the Company: Continental Hoop Tournament
Name: Marlow Teague
Position: Project Director
e-mail: marlow@hooptournamentx.com
mobile: +65 93718402
website: www.hooptournamentx.com
Address: 47 Brindle Road, #08-05, Singapore 917264
There is a picture attachted which can be used as a back side of the buisness card - we would like to follow the colors theme on the front card ( with the person contact details) how ever the front card we will prefer with white background but with graphfic elements coming from logo.
Updates
Project Deadline Extended
Reason: the project has been launched on 24 of April with deadline by 24 of April by mistakes. Thats why I would like to extend the deadline.
Name: Marlow Teague
mobile: +65 93718402

```html
<!DOCTYPE html>
<html lang="en">
<head>
<meta charset="utf-8">
<title>Continental Hoop Tournament – Business Card</title>
<link rel="stylesheet" href="https://fonts.googleapis.com/css2?family=Arimo:wght@400&display=swap">
<style>
  :root {
    --page: #ffffff;
    --frame-deep: #6b4423;
    --frame-glow: #d4a22a;
    --ink: #6a431f;
    --band: #7a4e22;
    --band-light: #e0b347;
    --paper: #ffffff;
  }
  * { margin: 0; padding: 0; box-sizing: border-box; }
  html, body {
    width: 1002px; height: 1200px; overflow: hidden;
    background: var(--page);
    font-family: "Arimo", Arial, sans-serif;
    color: var(--ink);
  }
  .canvas { position: relative; width: 1002px; height: 1200px; }
  .card {
    position: absolute; left: 27px; width: 948px; height: 545px;
    background:
      radial-gradient(ellipse 60% 55% at 50% 0%, var(--frame-glow), transparent 70%),
      radial-gradient(ellipse 60% 55% at 50% 100%, var(--frame-glow), transparent 70%),
      var(--frame-deep);
  }
  .card--front { top: 27px; }
  .card--back { top: 628px; }
  .card__paper {
    position: absolute; left: 54px; top: 57px; right: 52px; bottom: 55px;
    background: var(--paper);
  }
  .brand {
    position: absolute; left: 54px; top: 262px;
    display: flex; align-items: center; gap: 16px;
  }
  .brand__dot {
    width: 58px; height: 58px; border-radius: 50%;
    background: var(--band-light); flex: none;
  }
  .brand__name {
    font-size: 31px; line-height: 1.15; color: var(--ink);
    width: 230px;
  }
  .stripes { position: absolute; left: 313px; top: 277px; }
  .badge { position: absolute; left: 0; top: 152px; }
  .badge__name, .badge__role {
    position: absolute; left: 96px; color: #fff; white-space: nowrap;
  }
  .badge__name { top: 8px; font-size: 29px; }
  .badge__role { top: 65px; font-size: 21px; }
  .address { position: absolute; left: 109px; top: 293px; font-size: 21px; }
  .contacts {
    position: absolute; left: 109px; top: 337px;
    display: grid; grid-template-columns: 94px auto; row-gap: 3px;
    font-size: 21px; line-height: 26px;
  }
</style>
</head>
<body>
<div class="canvas">

  <section class="card card--front" aria-label="Front of business card">
    <div class="card__paper">
      <div class="brand">
        <span class="brand__dot"></span>
        <span class="brand__name">Continental Hoop Tournament</span>
      </div>
      <svg class="stripes" width="528" height="100" viewBox="0 0 528 100" aria-hidden="true">
        <g fill="var(--band)">
          <rect x="0" y="10" width="490" height="17"/>
          <rect x="0" y="33" width="490" height="17"/>
          <rect x="0" y="56" width="490" height="17"/>
          <rect x="0" y="79" width="490" height="17"/>
        </g>
        <g fill="var(--band-light)">
          <polygon points="490,10 528,2 528,18 505,27 490,27"/>
          <polygon points="490,33 528,25 528,41 505,50 490,50"/>
          <polygon points="490,56 528,48 528,64 505,73 490,73"/>
          <polygon points="490,79 528,71 528,87 505,96 490,96"/>
        </g>
      </svg>
    </div>
  </section>

  <section class="card card--back" aria-label="Back of business card">
    <div class="card__paper">
      <div class="badge">
        <svg width="353" height="100" viewBox="0 0 353 100" aria-hidden="true">
          <polygon points="0,0 85,0 85,43 0,28" fill="var(--band-light)"/>
          <rect x="85" y="0" width="268" height="43" fill="var(--band)"/>
          <polygon points="0,37 85,54 85,97 0,97" fill="var(--band-light)"/>
          <rect x="85" y="54" width="268" height="43" fill="var(--band)"/>
        </svg>
        <span class="badge__name">Marlow Teague</span>
        <span class="badge__role">Project Director</span>
      </div>
      <p class="address">47 Brindle Road, #08-05, Singapore 917264</p>
      <div class="contacts">
        <span>e-mail</span><span>: marlow@hooptournamentx.com</span>
        <span>mobile</span><span>: +65 93718402</span>
        <span>website</span><span>: www.hooptournamentx.com</span>
      </div>
    </div>
  </section>

</div>
</body>
</html>
```